Create Modern Clean Memorable Home Page

Please visit our current Homepage at www.brelvox.com. We want a fresh fun updated and memorable look. Feel free to use any of our photos if necessary. For more inspiration here are some other ice melt websites to browse:
http://www.quoralt.com/
http://www.pembrith.com/ice-melt/
http://www.globalvendrasalt.com/logistics.html
http://www.halvicsalt.com/
http://www.gubrine.com/
http://www.brinevaultco.com/gallery
http://www.thawfrost.com/products/calcium-chloride/
http://www.pelbranworks.com/dry-products
Updates
I have uploaded the logo
Just a note, we are not looking to simply display the product bags on the homepage. We want the first look at our page to pop and be memorable. We want color and possibly the use of photos with people and or animals and or landscapes to depict the use of the product. Most importantly it should be clean and not busy.
Industry/Entity Type
Logistics
Look and feel
Each slider illustrates characteristics of the customer's brand and the style your logo design should communicate.

```html
<!DOCTYPE html>
<html lang="en">
<head>
<meta charset="utf-8">
<title>Brelvox Seasonal Products</title>
<link href="https://fonts.googleapis.com/css2?family=Arimo:wght@400;700&family=Oswald:wght@500;700&display=swap" rel="stylesheet">
<style>
:root{
  --ink:#222;
  --navy:#0f2f55;
  --nav-bg:#bcdfee;
  --nav-active:#d6edf6;
  --hero-bg:#b9ddec;
  --tab:#2f8fd0;
  --tab-dark:#1a6fae;
  --accent:#2a9ad8;
  --orange:#f29a1a;
  --rule:#d8dde2;
}
*{margin:0;padding:0;box-sizing:border-box}
html,body{width:1200px;height:879px;overflow:hidden}
body{position:relative;background:#fff;font-family:"Arimo",Arial,sans-serif;color:var(--ink)}
.abs{position:absolute}

.topbar{left:0;top:0;width:1200px;height:75px;background:linear-gradient(#fff,#eef1f3)}
.utility{left:680px;top:0;display:flex;gap:2px}
.utility a{display:block;height:22px;padding:6px 0 0;text-align:center;background:linear-gradient(var(--tab),var(--tab-dark));color:#fff;font-size:9.5px;font-weight:700;text-decoration:none;border-radius:0 0 8px 8px;border:1px solid #0f5f98;border-top:0}
.utility a:nth-child(1){width:85px}
.utility a:nth-child(2){width:100px}
.utility a:nth-child(3){width:86px}
.callnow{right:245px;top:37px;display:flex;align-items:center;gap:5px;font-size:10.5px;font-weight:700;color:#444}
.callnow strong{font-size:15px;color:#111}

.mainnav{left:0;top:75px;width:1200px;height:40px;background:var(--nav-bg)}
.mainnav span{position:absolute;top:0;font-size:13px;color:var(--navy);line-height:40px;white-space:nowrap}
.mainnav .active{left:297px;width:92px;text-align:center;background:var(--nav-active)}

.hero{left:0;top:115px;width:1200px;height:243px;background:var(--hero-bg)}
.banner{left:294px;top:115px;width:677px;height:243px;background:linear-gradient(90deg,#dfeef8 0%,#9cc2e0 20%,#3f74b0 55%,#2a5c9c 100%);border-left:2px solid var(--navy)}
.hl{left:310px;color:var(--navy);font-family:"Oswald",Impact,sans-serif;text-transform:uppercase;white-space:nowrap}
.hl1{top:158px;font-size:19px;line-height:24px;font-weight:700}
.hl2{top:191px;font-size:14px;line-height:20px;font-weight:500}
.hl3{top:217px;font-size:25px;line-height:30px;font-weight:700}
.hl4{top:249px;font-size:29px;line-height:34px;font-weight:500}
.banner-text{left:310px;top:286px;width:330px;font-size:9.3px;line-height:12.5px;color:#1d3a5c}
.banner-more{left:310px;top:318px;font-size:10.5px;color:#fff}
.banner-photo{left:655px;top:154px;width:301px;height:181px;background:linear-gradient(#e4e9ee,#b9c3cc 55%,#8e9aa6);box-shadow:0 0 6px rgba(0,0,0,.35)}

.intro{left:296px;top:388px;width:443px;height:111px;border:1px solid var(--rule);border-radius:4px;background:linear-gradient(#fff 70%,#e8ebee);box-shadow:0 1px 2px rgba(0,0,0,.08)}
.intro h1{position:absolute;left:15px;top:11px;font-size:19px;font-weight:700;color:#2a2a2a}
.intro p{position:absolute;left:15px;top:38px;width:412px;font-size:8.1px;line-height:12px;color:#555}
.intro .more{position:absolute;right:18px;top:93px;font-size:9.5px;color:var(--navy)}

.col-title{font-size:14px;font-weight:400;color:#333}
.whatwedo{left:296px;top:515px;width:212px}
.whatwedo p{margin-top:12px;font-size:8.4px;line-height:14.1px;color:#111}
.whyus{left:520px;top:515px;width:190px}
.whyus h2{margin-left:7px}
.whyus ul{list-style:none;margin-top:13px}
.whyus li{position:relative;padding-left:12px;font-size:8.4px;line-height:11.5px;color:#555;margin-bottom:11px}
.whyus li svg{position:absolute;left:0;top:2px}

.productlist{left:762px;top:390px;width:206px;list-style:none}
.productlist li{height:29px;border:1px solid #d3d8dd;border-left:4px solid var(--navy);background:linear-gradient(#fafbfc,#e6eaee);font-size:10.5px;line-height:27px;padding-left:13px;color:#222;white-space:nowrap}
.productlist li.hover{border-left-color:var(--accent);background:linear-gradient(#f1f5f8,#dde4ea)}
.quote{left:759px;top:612px}
.quote .ask{font-size:10.6px;font-weight:700;color:#111}
.quote .num{font-size:20px;font-weight:700;color:var(--accent);margin-top:7px}

.footer{left:0;top:683px;width:1200px;height:162px;background:linear-gradient(#eaf0f5,#fff 40%);border-top:1px solid #e0e5ea;border-bottom:1px solid var(--rule)}
.fcol h3{font-size:11px;font-weight:700;color:#222;letter-spacing:.3px}
.fcontact{left:296px;top:698px}
.fcontact .brand{margin-top:8px;font-size:10.5px;font-weight:700;color:var(--accent);letter-spacing:.4px}
.fcontact .addr{margin-top:3px;font-size:9px;line-height:13px;color:#333}
.fcontact .lines{margin-top:10px;font-size:9px;line-height:17px;color:#333}
.fcontact .lines b{color:var(--orange)}
.fcontact .lines a{color:var(--accent);text-decoration:none}
.fproducts{left:529px;top:698px}
.fproducts ul{list-style:none;margin-top:6px}
.fproducts li{font-size:9px;line-height:16.8px;color:#333;padding-left:12px;position:relative}
.fproducts li::before{content:"";position:absolute;left:3px;top:5px;border-left:4px solid #333;border-top:3px solid transparent;border-bottom:3px solid transparent}
.fconnect{left:772px;top:698px}
.social{display:flex;gap:6px;margin-top:10px}
.social span{width:26px;height:26px;border-radius:50%;display:block}
.social .s1{background:#3b5c9a}.social .s2{background:#4ab3e0}.social .s3{background:#d8dde3}
.fconnect input{display:block;margin-top:12px;width:185px;height:20px;border:1px solid #6ab0dd}
.fconnect button{position:absolute;left:116px;top:86px;width:69px;height:17px;border:0;background:linear-gradient(#3aa4e4,#1f86c8);color:#fff;font-size:9px;font-family:inherit}

.copyright{left:296px;top:857px;font-size:9px;color:#333}
.copyright span{color:var(--accent)}
.legal{left:771px;top:857px;font-size:9px;color:#222}
.legal span{color:var(--accent)}
</style>
</head>
<body>

<div class="abs topbar"></div>
<nav class="abs utility"><a>CONTACT US</a><a>WAREHOUSE INFO</a><a>ABOUT US</a></nav>
<div class="abs callnow">
  <svg width="24" height="24" viewBox="0 0 24 24"><circle cx="12" cy="12" r="10" fill="none" stroke="#f2b01a" stroke-width="2.5"/><path d="M9 7c-1 2 0 6 3 9l2 1 1-2-2-2-1 1c-1-1-2-3-2-4l1-1-1-2z" fill="#222"/></svg>
  CALL US NOW: <strong>55 5014 273</strong>
</div>

<nav class="abs mainnav">
  <span class="active">HOME</span>
  <span style="left:404px">ICE MELTERS</span>
  <span style="left:522px">SHOVELS &amp; ICE CHOPPERS</span>
  <span style="left:721px">SALT SPREADERS</span>
  <span style="left:858px">SNOW TOOLS</span>
</nav>

<div class="abs hero"></div>
<div class="abs banner" role="img" aria-label="Snowy background with a snowdrop flower"></div>
<div class="abs hl hl1">Brelvox Seasonal Products Inc.</div>
<div class="abs hl hl2">To become your supplier with</div>
<div class="abs hl hl3">A quality product at</div>
<div class="abs hl hl4">A competitive price</div>
<p class="abs banner-text">We do the design, installation and maintenance of state-of-the-art structured cabling systems for voice, data, and fiber as well as related systems.</p>
<div class="abs banner-more">Learn More <svg width="7" height="8" viewBox="0 0 7 8"><path d="M0 0l7 4-7 4z" fill="#fff"/></svg></div>
<div class="abs banner-photo" role="img" aria-label="De-icer truck spreading salt on a snowy road lined with pine trees"></div>

<section class="abs intro">
  <h1>BRELVOX SEASONAL PRODUCTS,INC.</h1>
  <p>Brelvox Seasonal Products manufacturers and distributes a full line of packaged and bulk ice melting products. Our warehouse allows us to carry one of the largest packaged inventories in the Northeast enabling us to offer our customers a consistent supply of products. Our product line encompasses traditional ice melters, ice melt blends, green environmentally friendly ice melters and a full line of snow removal products.</p>
  <span class="more">Learn More <svg width="6" height="7" viewBox="0 0 6 7"><path d="M0 0l6 3.5-6 3.5z" fill="var(--accent)"/></svg></span>
</section>

<section class="abs whatwedo">
  <h2 class="col-title">WHAT WE DO</h2>
  <p>Customer satisfaction is our ultimate goal which is why we are constantly expanding and upgrading our product line availability based on customer feedback. We also provide around the clock availability during the winter season. Our customer base includes large retail outlets, wholesale clubs, supermarkets and discounted chain stores. It is no wonder that we continue to be one of the fastest growing companies in the industry. It's simple; we are good at what we do.</p>
</section>

<section class="abs whyus">
  <h2 class="col-title">WHY US</h2>
  <ul>
    <li><svg width="8" height="7" viewBox="0 0 8 7"><path d="M1 4l2 2 4-5" fill="none" stroke="#333" stroke-width="1.4"/></svg>Lorem ipsum dolor sit amet, consectetur adipiscing elit. Integer lectus.</li>
    <li><svg width="8" height="7" viewBox="0 0 8 7"><path d="M1 4l2 2 4-5" fill="none" stroke="#333" stroke-width="1.4"/></svg>Lorem ipsum dolor sit amet, consectetur adipiscing elit. Integer lectus.</li>
    <li><svg width="8" height="7" viewBox="0 0 8 7"><path d="M1 4l2 2 4-5" fill="none" stroke="#333" stroke-width="1.4"/></svg>Lorem ipsum dolor sit amet, consectetur adipiscing elit. Integer lectus.</li>
    <li><svg width="8" height="7" viewBox="0 0 8 7"><path d="M1 4l2 2 4-5" fill="none" stroke="#333" stroke-width="1.4"/></svg>Lorem ipsum dolor sit amet, consectetur adipiscing elit. Integer lectus.</li>
  </ul>
</section>

<ul class="abs productlist">
  <li>Calcium Magnesium Acetate (CMA)</li>
  <li>Embrite Pellets - Calcium Chloride</li>
  <li>KORVALT-Calcium Chloride Pellets</li>
  <li>Azure Thaw Snow &amp; Ice Melter</li>
  <li class="hover">Evergreen Path Snow &amp; Ice Melter</li>
  <li>Squall Premium Ice &amp; Snow Melter</li>
  <li>Rock Salt</li>
</ul>
<div class="abs quote">
  <div class="ask">CALL US FOR YOUR FREE QUOTE TODAY!</div>
  <div class="num">555-301-SNOW (7669)</div>
</div>

<footer class="abs footer"></footer>
<div class="abs fcol fcontact">
  <h3>CONTACT US</h3>
  <div class="brand">Brelvox Seasonal Products</div>
  <div class="addr">Q Block, Harlow Street<br>Kelbrook NSW 2391</div>
  <div class="lines"><b>T:</b> 55-501-427<br><b>F:</b> 55-50-1428<br><b>E:</b><a>info@BrelvoxSeasonal Products.com</a></div>
</div>
<div class="abs fcol fproducts">
  <h3>OUR PRODUCT</h3>
  <ul>
    <li>Calcium Magnesium Acetate (CMA)</li>
    <li>Embrite Pellets - Calcium Chloride</li>
    <li>KORVALT-Calcium Chloride Pellets</li>
    <li>Azure Thaw Snow &amp; Ice Melter</li>
    <li>Evergreen Path Snow &amp; Ice Melter</li>
    <li>Squall Premium Ice &amp; Snow Melter</li>
    <li>Rock Salt</li>
  </ul>
</div>
<div class="abs fcol fconnect">
  <h3>CONNECT WITH US</h3>
  <div class="social"><span class="s1"></span><span class="s2"></span><span class="s3"></span></div>
  <input type="text" aria-label="Email">
  <button>SUBMIT</button>
</div>

<div class="abs copyright">Copyright © 2013 <span>BrelvoxSeasonalProducts</span>. All Rights Reserved.</div>
<div class="abs legal"><span>Site Map</span> | Location &nbsp;| &nbsp;Privacy Policy | &nbsp;Career</div>

</body>
</html>
```